RWM Electrical Business Card Design

Have a logo to use, just looking for design around this, would like green theme, would like symbols in place of phone, fax, email etc.

Business

RWM Electrical, Marcus Thorley, marcus@rwmelectrical.example.au, www.rwmelectrical.example.au, mobile 0491 568 342, phone (07) 3915 4280, fax (07) 3915 4280, facebook and linkedin
addresses

```html
<!DOCTYPE html>
<html lang="en">
<head>
<meta charset="utf-8">
<title>RWM Electrical – Business Card</title>
<link rel="stylesheet" href="https://fonts.googleapis.com/css2?family=Carlito:wght@400;700&display=swap">
<style>
  :root {
    --card-black: #040507;
    --brand-green: #5fcf2e;
    --rule-green: #3f9e24;
    --streak-blue: #2f66c4;
    --streak-glow: #8fb4ff;
    --photo-tone: #6f6a66;
  }
  html, body {
    margin: 0;
    padding: 0;
    width: 1200px;
    height: 833px;
    overflow: hidden;
    background: #ffffff;
  }
  .card {
    position: relative;
    width: 1200px;
    height: 833px;
    background: var(--card-black);
    font-family: "Carlito", "Calibri", sans-serif;
    color: var(--brand-green);
    overflow: hidden;
  }
  .services {
    position: absolute;
    top: 28px;
    left: 0;
    width: 100%;
    text-align: center;
    font-size: 36px;
    margin: 0;
  }
  .services-rule {
    position: absolute;
    top: 88px;
    left: 50px;
    right: 36px;
    height: 3px;
    background: var(--rule-green);
  }
  .light-streaks {
    position: absolute;
    top: 130px;
    left: 0;
    width: 100%;
    height: 400px;
    background:
      radial-gradient(ellipse 60% 20% at 55% 45%, rgba(143,180,255,0.55), transparent 70%),
      radial-gradient(ellipse 75% 40% at 50% 50%, rgba(47,102,196,0.6), transparent 75%);
  }
  .brand {
    position: absolute;
    top: 270px;
    left: 0;
    width: 100%;
    display: flex;
    align-items: center;
    justify-content: center;
    gap: 28px;
  }
  .brand-mark {
    width: 100px;
    height: 100px;
    border-radius: 50%;
    background: var(--brand-green);
  }
  .brand-name {
    font-size: 84px;
    font-weight: 400;
    color: var(--brand-green);
    margin: 0;
  }
  .contact-row {
    position: absolute;
    top: 480px;
    left: 0;
    width: 100%;
    height: 160px;
  }
  .contact-name,
  .contact-mobile {
    position: absolute;
    top: 92px;
    font-size: 38px;
    margin: 0;
  }
  .contact-name { left: 70px; }
  .contact-mobile { right: 60px; }
  .portrait {
    position: absolute;
    left: 522px;
    top: 10px;
    width: 156px;
    height: 150px;
    background: linear-gradient(180deg, #3a3836 0%, var(--photo-tone) 55%, #d8d6d2 100%);
  }
  .details {
    position: absolute;
    top: 672px;
    left: 50px;
    right: 36px;
    border-top: 3px solid var(--rule-green);
    padding-top: 22px;
    display: flex;
    flex-direction: column;
    gap: 16px;
  }
  .details-line {
    display: flex;
    justify-content: center;
    gap: 48px;
    margin: 0;
    font-size: 26px;
  }
  .detail {
    display: flex;
    align-items: center;
    gap: 10px;
    white-space: nowrap;
  }
  .detail svg {
    width: 26px;
    height: 26px;
    fill: none;
    stroke: var(--brand-green);
    stroke-width: 2;
    stroke-linejoin: round;
    stroke-linecap: round;
  }
  .social-dot {
    width: 20px;
    height: 20px;
    background: var(--brand-green);
  }
</style>
</head>
<body>
  <main class="card">
    <p class="services">Commerical, Domestic, Civil, and Service</p>
    <div class="services-rule"></div>

    <div class="light-streaks" role="img" aria-label="Flowing blue light streaks across the card"></div>

    <div class="brand">
      <span class="brand-mark"></span>
      <h1 class="brand-name">RWM Electrical</h1>
    </div>

    <div class="contact-row">
      <p class="contact-name">Marcus Thorley</p>
      <div class="portrait" role="img" aria-label="Portrait photo of Marcus Thorley"></div>
      <p class="contact-mobile">Mobile 0491 568 342</p>
    </div>

    <section class="details">
      <p class="details-line">
        <span class="detail">
          <svg viewBox="0 0 24 24" aria-hidden="true"><path d="M5 3h4l2 5-3 2a12 12 0 0 0 6 6l2-3 5 2v4a2 2 0 0 1-2 2A17 17 0 0 1 3 5a2 2 0 0 1 2-2z"/></svg>
          (07) 3915 4280
        </span>
        <span class="detail">
          <svg viewBox="0 0 24 24" aria-hidden="true"><rect x="3" y="9" width="18" height="10" rx="1"/><path d="M7 9V3h10v6M7 15h10"/></svg>
          (07) 3915 4280
        </span>
        <span class="detail">
          <span class="social-dot"></span>
          /rwmelectrical
        </span>
      </p>
      <p class="details-line">
        <span class="detail">
          <svg viewBox="0 0 24 24" aria-hidden="true"><rect x="2" y="5" width="20" height="14" rx="1"/><path d="M2 6l10 7 10-7"/></svg>
          marcus@rwmelectrical.example.au
        </span>
        <span class="detail">
          <svg viewBox="0 0 24 24" aria-hidden="true"><circle cx="12" cy="12" r="9"/><path d="M3 12h18M12 3c3 3 3 15 0 18M12 3c-3 3-3 15 0 18"/></svg>
          www.rwmelectrical.example.au
        </span>
        <span class="detail">
          <span class="social-dot"></span>
          /marcus-thorley
        </span>
      </p>
    </section>
  </main>
</body>
</html>
```